Income Tax Flyer - Updates Needed

Just need to update this flyer design and give it a new look. We would like to keep all the same wording but make it stand out a little more. Our selling point is the "Same Day Tax Advance up to $6,000"

Industry/Entity Type

Lending, Small Loans, Tax Services, Title Loans, Personal Loans

```html
<!DOCTYPE html>
<html lang="en">
<head>
<meta charset="utf-8">
<title>Ledgerline Financial Group – Easy Advance Flyer</title>
<link rel="stylesheet" href="https://fonts.googleapis.com/css2?family=Heebo:wght@400;500;600;700;800&family=Roboto+Condensed:wght@700&display=swap">
<style>
  :root {
    --page-bg: #4f4f4f;
    --paper: #fcf7f3;
    --green: #13693a;
    --green-dark: #155130;
    --red: #c8161d;
    --ink: #151515;
    --line: #222;
  }
  * { margin: 0; padding: 0; box-sizing: border-box; }
  html, body {
    width: 973px; height: 1200px; overflow: hidden;
    background: var(--page-bg);
  }
  .flyer {
    position: absolute; left: 98px; top: 0;
    width: 776px; height: 1200px;
    background: var(--paper);
    overflow: hidden;
    font-family: "Heebo", sans-serif;
    color: var(--ink);
  }
  .flyer-shapes { position: absolute; inset: 0; width: 776px; height: 1200px; }
  .brand {
    position: absolute; top: 78px; left: 0; width: 100%;
    text-align: center;
    font-weight: 600; font-size: 30px; color: var(--green);
    letter-spacing: 0.5px;
  }
  .apply-tag {
    position: absolute; left: 199px; top: 194px; width: 379px; height: 45px;
    background: linear-gradient(90deg, var(--green-dark), var(--green) 50%, var(--green-dark));
    border-radius: 6px;
    box-shadow: 0 0 0 2px #fff;
    color: #fff; text-align: center;
    font-weight: 500; font-size: 45px; line-height: 47px; letter-spacing: -0.5px;
  }
  .apply-shadow {
    position: absolute; left: 230px; top: 243px; width: 320px; height: 8px;
    background: radial-gradient(ellipse at center, rgba(0,0,0,0.35), rgba(0,0,0,0) 70%);
  }
  .offer-amount {
    position: absolute; top: 256px; left: 0; width: 100%; text-align: center;
    font-family: "Roboto Condensed", sans-serif; font-weight: 700;
    font-size: 54px; line-height: 60px; color: var(--red);
  }
  .pitch {
    position: absolute; top: 735px; left: 0; width: 100%; text-align: center;
    font-size: 38px; line-height: 48px; font-weight: 500; letter-spacing: -0.3px;
  }
  .pitch-highlight {
    position: absolute; top: 790px; left: 0; width: 100%; text-align: center;
    font-family: "Roboto Condensed", sans-serif; font-weight: 700;
    font-size: 54px; line-height: 64px; color: var(--red);
  }
  .feature-label {
    position: absolute; top: 978px; width: 180px; margin-left: -90px;
    text-align: center; font-size: 19px; line-height: 24px;
  }
  .feature-label.speed { left: 158px; }
  .feature-label.amount { left: 388px; }
  .feature-label.ease { left: 617px; }
  .phone {
    position: absolute; left: 57px; top: 1060px;
    font-size: 37px; font-weight: 500; line-height: 44px; letter-spacing: -0.3px;
  }
  .address-label {
    position: absolute; left: 54px; top: 1168px;
    transform: rotate(-90deg); transform-origin: left top;
    font-size: 8px; line-height: 9px; letter-spacing: 1.5px; white-space: nowrap;
  }
  .cta {
    position: absolute; left: 457px; top: 1140px;
    font-size: 28px; line-height: 34px; color: #fff; font-weight: 400;
  }
  .cta strong { font-weight: 700; }
</style>
</head>
<body>
<main class="flyer">
  <svg class="flyer-shapes" viewBox="0 0 1255 1940" preserveAspectRatio="none">
    <defs>
      <linearGradient id="photoTone" x1="0" y1="0" x2="0" y2="1">
        <stop offset="0" stop-color="#f3ebe4" stop-opacity="0"/>
        <stop offset="0.2" stop-color="#ece2d8" stop-opacity="0.85"/>
        <stop offset="0.6" stop-color="#e4dbd3"/>
        <stop offset="1" stop-color="#d9cfc5"/>
      </linearGradient>
      <linearGradient id="bandGreen" x1="0" y1="0" x2="1" y2="0">
        <stop offset="0" stop-color="#165130"/>
        <stop offset="0.6" stop-color="#13693a"/>
        <stop offset="1" stop-color="#155a33"/>
      </linearGradient>
      <linearGradient id="footGreen" x1="0" y1="0" x2="1" y2="0">
        <stop offset="0" stop-color="#155130"/>
        <stop offset="0.5" stop-color="#137040"/>
        <stop offset="1" stop-color="#13693a"/>
      </linearGradient>
    </defs>

    <path class="hero-photo" role="img" aria-label="Photo: smiling woman in a striped blouse reviewing tax documents in a bright living room"
          d="M0,470 L1255,470 L1255,870 Q600,1140 0,1020 Z" fill="url(#photoTone)"/>

    <path class="swoosh-band" d="M0,1020 Q600,1140 1255,870 L1255,913 Q600,1225 0,1118 Z" fill="url(#bandGreen)"/>
    <path class="swoosh-accent" d="M380,1078 Q800,1130 1255,870 L1255,886 Q800,1146 380,1084 Z" fill="var(--red)"/>

    <line class="timeline" x1="102" y1="1491" x2="1154" y2="1491" stroke="var(--line)" stroke-width="2"/>
    <circle cx="102" cy="1491" r="5" fill="var(--line)"/>
    <circle cx="1154" cy="1491" r="5" fill="var(--line)"/>

    <g class="feature-box" fill="var(--paper)" stroke="#333" stroke-width="1.5">
      <rect x="185" y="1430" width="126" height="126" rx="10"/>
      <rect x="564" y="1430" width="126" height="126" rx="10"/>
      <rect x="944" y="1430" width="126" height="126" rx="10"/>
    </g>

    <g class="icon-stopwatch" fill="none" stroke="var(--red)" stroke-width="5">
      <circle cx="250" cy="1500" r="30"/>
      <rect x="240" y="1455" width="20" height="9" rx="3" fill="var(--red)"/>
      <line x1="250" y1="1464" x2="250" y2="1470"/>
      <path d="M268,1468 L280,1474" stroke-width="4"/>
    </g>
    <text x="250" y="1512" text-anchor="middle" font-family="Heebo, sans-serif" font-weight="700" font-size="32" fill="var(--red)">$</text>

    <g class="icon-cash">
      <rect x="595" y="1470" width="64" height="38" rx="4" fill="var(--red)" transform="rotate(-8 627 1489)"/>
      <circle cx="627" cy="1490" r="11" fill="#fff"/>
      <text x="627" y="1497" text-anchor="middle" font-family="Heebo, sans-serif" font-weight="700" font-size="18" fill="var(--red)">$</text>
      <path d="M642,1500 L642,1530 Q642,1538 650,1538 L662,1538 Q668,1538 668,1530 L668,1514 L650,1510 L650,1500 Q646,1494 642,1500 Z" fill="#fff" stroke="var(--red)" stroke-width="2.5"/>
    </g>

    <g class="icon-bag">
      <path d="M1000,1466 Q990,1480 993,1494 Q997,1506 1010,1506 Q1023,1506 1027,1494 Q1030,1480 1020,1466 Z" fill="var(--red)"/>
      <rect x="1003" y="1456" width="14" height="8" rx="2" fill="var(--red)"/>
      <text x="1010" y="1498" text-anchor="middle" font-family="Heebo, sans-serif" font-weight="700" font-size="18" fill="#fff">$</text>
      <path d="M980,1530 Q992,1514 1010,1522 L1030,1522 Q1044,1518 1050,1512 Q1046,1526 1030,1532 L1000,1536 Z" fill="none" stroke="var(--red)" stroke-width="3"/>
    </g>

    <path class="icon-pin" fill="var(--ink)" fill-rule="evenodd"
          d="M96,1832 C90,1824 87,1819 87,1815 A9,9 0 1 1 105,1815 C105,1819 102,1824 96,1832 Z M96,1811 A4,4 0 1 0 96.01,1811 Z"/>
    <g class="address-lines" stroke="var(--red)" stroke-width="2">
      <line x1="116" y1="1811" x2="441" y2="1811"/>
      <line x1="116" y1="1851" x2="441" y2="1851"/>
      <line x1="116" y1="1889" x2="441" y2="1889"/>
    </g>

    <path class="footer-swoosh" d="M491,1940 Q820,1760 1255,1785 L1255,1940 Z" fill="url(#footGreen)"/>
  </svg>

  <div class="brand">Ledgerline Financial Group</div>

  <div class="apply-tag">APPLY HERE FOR</div>
  <div class="apply-shadow"></div>
  <h1 class="offer-amount">$5,000-$6,000 TODAY!</h1>

  <p class="pitch">File your taxes and apply for an</p>
  <h2 class="pitch-highlight">EASY ADVANCE</h2>

  <p class="feature-label speed">Available in<br>24 Hours or Less</p>
  <p class="feature-label amount">Choose Your<br>Loan Amount</p>
  <p class="feature-label ease">Quick and<br>Easy</p>

  <p class="phone">+001 555 0190</p>
  <span class="address-label">Adress</span>

  <p class="cta">CONTRACT US <strong>TODAY!</strong></p>
</main>
</body>
</html>
```